Banner Ad Design Project

We need banner ads for a website size:
728 x 90
160 x 90

Look at our website and you can see the color green we use throughout our advertising.

We have copy for 4 ads that should be interchangable

1. EHR me ASAP. Sign up in minutes.
2. Connect. Collaborate. Immediate. Sign up in minutes.
3. No software. No downloads. No charge.
4. EMR + HIE + PMR = FREE

Target Market(s)

Physicians

Industry/Entity Type

Software

```html
<!DOCTYPE html>
<html lang="en">
<head>
<meta charset="utf-8">
<title>Sign-up Banner Set</title>
<link rel="stylesheet" href="https://fonts.googleapis.com/css2?family=PT+Sans:ital,wght@1,400;1,700&display=swap">
<style>
  :root {
    --canvas: #ffffff;
    --gold-top: #ffd21c;
    --gold-mid: #ffbb00;
    --orange-band: #ffa200;
    --orange-low: #ff8a00;
    --edge-dark: #8f4c06;
    --edge-light: #ffe680;
    --tile-top: #f7b62e;
    --tile-mid: #f5a623;
    --tile-band: #f39526;
    --tile-low: #ef8420;
    --tile-edge: #c2621a;
    --ribbon-top: #5cb2ee;
    --ribbon-low: #1e6fb8;
    --ribbon-fold: #174f86;
    --ink: #ffffff;
    --icon-cream: #ffe8c4;
  }
  html, body {
    margin: 0;
    padding: 0;
    width: 1200px;
    height: 1200px;
    overflow: hidden;
    background: var(--canvas);
  }
  .canvas {
    position: relative;
    width: 1200px;
    height: 1200px;
    font-family: "PT Sans", "Trebuchet MS", sans-serif;
    font-style: italic;
    font-weight: 700;
    color: var(--ink);
  }
  .leaderboard {
    position: absolute;
    width: 967px;
    height: 111px;
    border-radius: 4px;
    border-top: 2px solid var(--edge-light);
    border-bottom: 5px solid var(--edge-dark);
    background: linear-gradient(to bottom,
      var(--gold-top) 0%, var(--gold-mid) 48%,
      var(--orange-band) 49%, var(--orange-low) 100%);
    box-shadow: inset 0 0 0 1px rgba(255,255,255,0.25);
  }
  .leaderboard .icon {
    position: absolute;
    left: 18px;
    top: 50%;
    transform: translateY(-50%);
  }
  .headline, .tagline, .single-line {
    position: absolute;
    margin: 0;
    white-space: nowrap;
    text-shadow: 0 2px 3px rgba(150,70,0,0.45);
    line-height: 1;
  }
  .ad-ehr { left: 117px; top: 35px; }
  .ad-ehr .headline { left: 128px; top: 6px; font-size: 60px; }
  .ad-ehr .tagline { right: 24px; top: 56px; font-size: 44px; }

  .ad-connect { left: 112px; top: 195px; }
  .ad-connect .headline { left: 132px; top: 6px; font-size: 56px; font-weight: 400; letter-spacing: 0.5px; }
  .ad-connect .tagline { right: 24px; top: 58px; font-size: 44px; }

  .ad-nosoftware { left: 117px; top: 357px; }
  .ad-nosoftware .single-line { left: 144px; top: 31px; font-size: 45px; font-weight: 400; }

  .ad-free { left: 117px; top: 519px; }
  .ad-free .single-line { left: 189px; top: 21px; font-size: 66px; font-weight: 400; }

  .tile {
    position: absolute;
    width: 203px;
    height: 117px;
    border-radius: 3px;
    border-top: 2px solid #fbd77a;
    border-bottom: 4px solid var(--tile-edge);
    background: linear-gradient(to bottom,
      var(--tile-top) 0%, var(--tile-mid) 46%,
      var(--tile-band) 47%, var(--tile-low) 100%);
    text-align: center;
  }
  .tile-text {
    margin: 0;
    line-height: 1.05;
    text-shadow: 0 1px 2px rgba(150,70,0,0.4);
  }
  .tile-ehr { left: 309px; top: 757px; }
  .tile-ehr .tile-text { padding-top: 28px; font-size: 27px; }
  .tile-connect { left: 609px; top: 752px; }
  .tile-connect .tile-text { padding-top: 6px; font-size: 21px; line-height: 0.98; }
  .tile-nosoftware { left: 315px; top: 939px; }
  .tile-nosoftware .tile-text { padding-top: 17px; font-size: 23px; line-height: 1.22; }
  .tile-free { left: 612px; top: 932px; }
  .tile-free .tile-text { padding-top: 18px; font-size: 22px; line-height: 1.25; }

  .ribbon {
    position: absolute;
    left: 22px;
    width: 190px;
    height: 32px;
  }
  .tile-ehr .ribbon { top: 72px; }
  .tile-connect .ribbon { top: 74px; }
  .ribbon-label {
    position: absolute;
    left: 0;
    top: 4px;
    width: 182px;
    text-align: center;
    font-size: 18px;
    font-weight: 700;
    line-height: 1;
    text-shadow: 0 1px 1px rgba(0,40,90,0.5);
  }
</style>
</head>
<body>
<div class="canvas">

  <!-- Leaderboard 1 -->
  <section class="leaderboard ad-ehr">
    <svg class="icon" width="90" height="90" viewBox="0 0 90 90" aria-hidden="true">
      <g fill="#ffffff">
        <path d="M40 14 L70 30 L58 46 L48 60 L38 52 L34 42 Z"/>
        <rect x="22" y="68" width="48" height="3"/>
      </g>
      <path d="M30 66 L44 50" stroke="var(--orange-band)" stroke-width="4"/>
      <circle cx="45" cy="48" r="4" fill="var(--orange-band)"/>
      <path d="M28 68 L38 52" stroke="#ffffff" stroke-width="3"/>
    </svg>
    <h2 class="headline">EHR me ASAP</h2>
    <p class="tagline">Sign up in minutes</p>
  </section>

  <!-- Leaderboard 2 -->
  <section class="leaderboard ad-connect">
    <svg class="icon" width="90" height="90" viewBox="0 0 90 90" aria-hidden="true">
      <g fill="none" stroke="#ffffff" stroke-width="7" stroke-linecap="round">
        <path d="M20 38 A26 26 0 0 1 36 20"/>
        <path d="M54 18 A26 26 0 0 1 72 36"/>
        <path d="M72 54 A26 26 0 0 1 54 72"/>
        <path d="M36 72 A26 26 0 0 1 18 54"/>
      </g>
      <g fill="#ffffff">
        <path d="M30 12 L44 20 L30 28 Z"/>
        <path d="M80 30 L72 44 L64 30 Z"/>
        <path d="M60 80 L46 72 L60 64 Z"/>
        <path d="M10 60 L18 46 L26 60 Z"/>
      </g>
    </svg>
    <h2 class="headline">Connect·Collaborate·Immediate</h2>
    <p class="tagline">Sign up in minutes</p>
  </section>

  <!-- Leaderboard 3 -->
  <section class="leaderboard ad-nosoftware">
    <svg class="icon" width="80" height="70" viewBox="0 0 80 70" aria-hidden="true">
      <path d="M10 24 L22 14 L40 32 L58 14 L70 24 L40 54 Z" fill="var(--icon-cream)" stroke="#f08a00" stroke-width="3" stroke-linejoin="round"/>
    </svg>
    <p class="single-line">No software · No downloads · No charge</p>
  </section>

  <!-- Leaderboard 4 -->
  <section class="leaderboard ad-free">
    <svg class="icon" width="80" height="100" viewBox="0 0 80 100" aria-hidden="true">
      <path d="M10 20 L22 10 L40 28 L58 10 L70 20 L40 50 Z" fill="var(--icon-cream)" stroke="#f08a00" stroke-width="3" stroke-linejoin="round"/>
      <path d="M10 50 L22 40 L40 58 L58 40 L70 50 L40 80 Z" fill="var(--icon-cream)" stroke="#f08a00" stroke-width="3" stroke-linejoin="round"/>
    </svg>
    <p class="single-line">EMR + HIE + PMR = FREE</p>
  </section>

  <!-- Small tiles -->
  <section class="tile tile-ehr">
    <p class="tile-text">EHR me ASAP</p>
    <div class="ribbon">
      <svg width="190" height="32" viewBox="0 0 190 32" aria-hidden="true">
        <defs>
          <linearGradient id="ribbon-fill-a" x1="0" y1="0" x2="0" y2="1">
            <stop offset="0" stop-color="var(--ribbon-top)"/>
            <stop offset="1" stop-color="var(--ribbon-low)"/>
          </linearGradient>
        </defs>
        <path d="M178 4 L190 4 L186 16 L190 30 L176 30 Z" fill="var(--ribbon-fold)"/>
        <rect x="0" y="2" width="182" height="26" rx="13" fill="url(#ribbon-fill-a)"/>
      </svg>
      <span class="ribbon-label">Sign up in minutes</span>
    </div>
  </section>

  <section class="tile tile-connect">
    <p class="tile-text">Connect<br>Collaborate<br>Immediate</p>
    <div class="ribbon">
      <svg width="190" height="32" viewBox="0 0 190 32" aria-hidden="true">
        <defs>
          <linearGradient id="ribbon-fill-b" x1="0" y1="0" x2="0" y2="1">
            <stop offset="0" stop-color="var(--ribbon-top)"/>
            <stop offset="1" stop-color="var(--ribbon-low)"/>
          </linearGradient>
        </defs>
        <path d="M178 4 L190 4 L186 16 L190 30 L176 30 Z" fill="var(--ribbon-fold)"/>
        <rect x="0" y="2" width="182" height="26" rx="13" fill="url(#ribbon-fill-b)"/>
      </svg>
      <span class="ribbon-label">Sign up in minutes</span>
    </div>
  </section>

  <section class="tile tile-nosoftware">
    <p class="tile-text">No software<br>No downloads<br>No charge</p>
  </section>

  <section class="tile tile-free">
    <p class="tile-text">EMR + HIE + PMR<br>=<br>FREE</p>
  </section>

</div>
</body>
</html>
```